Business cards - KESTO Roofing & Siding

We need simple business cards made up for our Roofing & Siding business based in Calgary Alberta.
The logo on one side of the card and potentially our slogan "Built with trust, verified by time".
The other side could have:
-A small logo
-Rep name:
-Rep cell phone:
-Rep email:
-Office phone: 403-386-2049
-Website: PrairieShinglePros.com

We would like to incorporate the colours from our logo, especially the lite blue on the jpeg file. I have attached the ai file and jpeg file. We like the colours better on the jpeg file.

I do not require a money back guarantee

```html
<!DOCTYPE html>
<html lang="en">
<head>
<meta charset="utf-8">
<title>KESTO Roofing &amp; Siding – Business Cards</title>
<link href="https://fonts.googleapis.com/css2?family=Cabin:ital,wght@0,400;0,600;1,400&display=swap" rel="stylesheet">
<style>
  :root {
    --backdrop: #5f5f5f;
    --brand-blue: #5182c0;
    --card-white: #ffffff;
    --ink-dark: #111111;
    --label-ink: #0a0a0a;
  }
  html, body {
    margin: 0;
    padding: 0;
    width: 1200px;
    height: 947px;
    overflow: hidden;
    background: var(--backdrop);
    font-family: "Cabin", sans-serif;
  }
  .sheet {
    position: relative;
    width: 1200px;
    height: 947px;
  }
  .side-label {
    position: absolute;
    margin: 0;
    font-size: 23px;
    font-weight: 400;
    color: var(--label-ink);
    line-height: 1;
  }
  .side-label--back { left: 29px; top: 12px; }
  .side-label--front { right: 47px; top: 416px; }

  .card {
    position: absolute;
    width: 813px;
    height: 465px;
    background: var(--card-white);
    box-shadow: 4px 4px 6px rgba(0,0,0,0.45);
    overflow: hidden;
  }
  .card--front { left: 350px; top: 450px; }
  .card--back { left: 25px; top: 40px; z-index: 2; }

  .card__band {
    position: absolute;
    inset: 0;
    width: 813px;
    height: 465px;
  }
  .card__band polygon { fill: var(--brand-blue); }

  .slogan {
    position: absolute;
    left: 40px;
    top: 218px;
    margin: 0;
    font-size: 22px;
    font-weight: 400;
    color: var(--card-white);
  }

  .wordmark {
    position: absolute;
    text-align: center;
    font-weight: 600;
    margin: 0;
  }
  .wordmark span { display: block; }
  .wordmark--large {
    left: 421px;
    top: 185px;
    width: 364px;
    color: var(--ink-dark);
  }
  .wordmark--large .wordmark__name { font-size: 84px; letter-spacing: 0.08em; line-height: 1; }
  .wordmark--large .wordmark__trade { font-size: 29px; letter-spacing: 0.2em; line-height: 1.4; }
  .wordmark--small {
    left: 585px;
    top: 52px;
    width: 200px;
    color: var(--card-white);
  }
  .wordmark--small .wordmark__name { font-size: 46px; letter-spacing: 0.08em; line-height: 1; }
  .wordmark--small .wordmark__trade { font-size: 16px; letter-spacing: 0.2em; line-height: 1.5; }

  .contact {
    position: absolute;
    left: 37px;
    top: 262px;
    margin: 0;
    color: var(--brand-blue);
    font-style: normal;
  }
  .contact__name {
    margin: 0 0 2px;
    font-size: 39px;
    font-style: italic;
    font-weight: 400;
    line-height: 1.05;
  }
  .contact__line {
    margin: 0;
    font-size: 23px;
    line-height: 29.3px;
  }
</style>
</head>
<body>
<main class="sheet">
  <p class="side-label side-label--back">Back</p>
  <p class="side-label side-label--front">Front</p>

  <section class="card card--back" aria-label="Card back">
    <svg class="card__band" viewBox="0 0 813 465" aria-hidden="true">
      <polygon points="0,0 607,0 213,465 0,465"/>
    </svg>
    <p class="slogan">Built with trust, verified by time.</p>
    <h1 class="wordmark wordmark--large">
      <span class="wordmark__name">KESTO</span>
      <span class="wordmark__trade">ROOFING &amp; SIDING</span>
    </h1>
  </section>

  <section class="card card--front" aria-label="Card front">
    <svg class="card__band" viewBox="0 0 813 465" aria-hidden="true">
      <polygon points="253,0 813,0 813,465 601,465"/>
    </svg>
    <p class="wordmark wordmark--small">
      <span class="wordmark__name">KESTO</span>
      <span class="wordmark__trade">ROOFING &amp; SIDING</span>
    </p>
    <address class="contact">
      <h2 class="contact__name">Mark Kesto</h2>
      <p class="contact__line">C: 403-555-0142</p>
      <p class="contact__line">E: Mark@prairieshinglepros.com</p>
      <p class="contact__line">O: 403-386-2049</p>
      <p class="contact__line">W: PrairieShinglePros.com</p>
    </address>
  </section>
</main>
</body>
</html>
```